Labels design for a a range of food products

We are looking for labels design for a range of food product. The design should be the same for all the label with brown/black background and gold and white wording like the one attached.
The size and the content of the label will change depending on the different products.
I have also attached the logo to be used which is the logo "CORVANE" Telmora. You shall be using the black and gold version. Brighter/shining gold is better.
The first label to be designed is the one related a plastic tray like the one Cappelletti" file: IMG_20151231_021838
The second label to be designed is the one related to a bottle like the one "Olive Oil" file; IMG_20151231_021651
The third label to be designed is the one related to a jar like the one "Olive Taggiasche" file: IMG_20151231_021531 and IMG_20151231_021549
The fourth label to be designed is the one related to bag like the one IMG_20151231_021506
The fifth label to be designed is the one related to the bottle. IMG_20151231_021426_panorama
This files are only samples. I have attached a file excel "Texts for Labels" in which you will find the text to be applied for the labels.
In order to decide the best design a front and a back label should be provided.

Food Consumers

Product

• Front and Back Label
• Some pictures of the product on the label would be nice to have to recall what is inside.

```html
<!DOCTYPE html>
<html lang="it">
<head>
<meta charset="utf-8">
<title>Etichetta retro – Olio extravergine di oliva DOP</title>
<link href="https://fonts.googleapis.com/css2?family=Jost:wght@300;400&display=swap" rel="stylesheet">
<style>
  :root {
    --label-bg: #0b0b0b;
    --ink: #f2f2f2;
    --rule: #e6e6e6;
    --blank: #ffffff;
    --gold: #c9a24a;
  }
  html, body {
    margin: 0;
    padding: 0;
    width: 1200px;
    height: 3904px;
    overflow: hidden;
    background: var(--label-bg);
  }
  .back-label {
    position: relative;
    width: 1200px;
    height: 3904px;
    background: var(--label-bg);
    color: var(--ink);
    font-family: "Jost", sans-serif;
    font-weight: 300;
  }
  .intro {
    position: absolute;
    left: 112px;
    top: 64px;
    width: 1000px;
    margin: 0;
    font-size: 54px;
    line-height: 76px;
  }
  .storage {
    position: absolute;
    left: 112px;
    top: 672px;
    width: 1000px;
    margin: 0;
    font-size: 54px;
    line-height: 76px;
  }
  .nutrition {
    position: absolute;
    left: 112px;
    top: 1288px;
    width: 1008px;
    border-collapse: collapse;
    font-size: 44px;
    line-height: 56px;
  }
  .nutrition td {
    border: 3px solid var(--rule);
    padding: 0 20px;
    vertical-align: middle;
    height: 92px;
  }
  .nutrition .label-col { width: 720px; }
  .nutrition .head td { height: 106px; }
  .nutrition .energy td { height: 166px; }
  .nutrition .energy .label-col { vertical-align: top; padding-top: 18px; }
  .nutrition .energy .value span { display: block; }
  .nutrition .footnote td {
    height: 92px;
    text-align: center;
    font-size: 34px;
  }
  .best-before {
    position: absolute;
    left: 0;
    top: 2624px;
    width: 1200px;
    margin: 0;
    text-align: center;
    font-size: 46px;
  }
  .date-field {
    position: absolute;
    left: 144px;
    top: 2752px;
    width: 912px;
    height: 148px;
    background: var(--blank);
  }
  .producer {
    position: absolute;
    left: 0;
    top: 3064px;
    width: 1200px;
    margin: 0;
    text-align: center;
    font-size: 44px;
    line-height: 96px;
  }
  .brand {
    position: absolute;
    left: 150px;
    top: 3570px;
    display: flex;
    align-items: center;
    gap: 24px;
    color: var(--gold);
    font-size: 44px;
    font-weight: 400;
  }
  .brand-dot {
    width: 72px;
    height: 72px;
    border-radius: 50%;
    background: var(--gold);
  }
  .volume {
    position: absolute;
    right: 88px;
    top: 3690px;
    font-size: 60px;
  }
</style>
</head>
<body>
<main class="back-label">
  <p class="intro">L'olio extravergine di oliva a cui viene riconosciuto il marchio DOP a tutela e garanzia del consumatore ha superato tutti i controlli di laboratorio e di prove di assaggio (PANEL TEST) operate da strutture esterne alla produzione.</p>

  <p class="storage">Modalità di conservazione:<br>Conservare in luogo fresco, al riparo dalla luce e da fonti di calore.</p>

  <table class="nutrition">
    <tr class="head"><td class="label-col">Valori nutrizionali medi per</td><td>100ml</td></tr>
    <tr class="energy"><td class="label-col">Energia</td><td class="value"><span>3389 kj</span><span>824kcal</span></td></tr>
    <tr><td class="label-col">Grassi</td><td>91,6 g</td></tr>
    <tr><td class="label-col">di cui acidi saturi</td><td>14,1 g</td></tr>
    <tr><td class="label-col">di cui acidi grassi monoinsaturi</td><td>68,3 g</td></tr>
    <tr><td class="label-col">di cui acidi grassi polinsaturi</td><td>9,2 g</td></tr>
    <tr><td class="label-col">Carboidrati</td><td>0,0 g</td></tr>
    <tr><td class="label-col">di cui zuccheri</td><td>0,0 g</td></tr>
    <tr><td class="label-col">Fibre</td><td>0,0 g</td></tr>
    <tr><td class="label-col">Proteine</td><td>0,0 g</td></tr>
    <tr><td class="label-col">Sale</td><td>0,0g</td></tr>
    <tr class="footnote"><td colspan="2">* RI=Assunzioni di riferimento di un adulto medio</td></tr>
  </table>

  <p class="best-before">Da consumarsi preferibilmente entro il:</p>
  <div class="date-field"></div>

  <p class="producer">Prodotto e imbottigliato all'origine per<br>VERDALIS S.r.l. - C.da Olmaia 4/B<br>Lorvento (BR) - Italy nello stabilimento<br>di Via dei Frantoi 27/A Lorvento (BR)</p>

  <div class="brand"><span class="brand-dot"></span><span class="brand-name">"CORVANE" Telmora</span></div>

  <div class="volume">750ml</div>
</main>
</body>
</html>
```